" A empresa tem como principal atrativo a grande variedade de joias infantis. Nosso maior diferencial são as peças de alta joalheria para crianças e a confecção de joias exclusivas e personalizadas para o publico de todas as idades. Temos um atelier para atendimento com hora marcada e o e-commerce é nossa principal vitrine. É possível conhecer algumas peças e parte da identidade da marca no nosso site www.brilhomirim.com.br e no instagram @brilhomirim "

```html
<!DOCTYPE html>
<html lang="pt-BR">
<head>
<meta charset="utf-8">
<title>Brilho Mirim — Cartão de visita</title>
<link rel="stylesheet" href="https://fonts.googleapis.com/css2?family=Josefin+Sans:wght@400;600&family=Open+Sans:wght@400&family=Great+Vibes&display=swap">
<style>
  :root {
    --bg: #eeeeee;
    --card: #ffffff;
    --accent: #8ecfe0;
    --brand: #5fa9bf;
    --text: #7b7b7b;
    --text-light: #9a9a9a;
    --shadow: rgba(0, 0, 0, 0.12);
  }
  * { margin: 0; padding: 0; box-sizing: border-box; }
  html, body { width: 1200px; height: 1200px; overflow: hidden; }
  body { background: var(--bg); position: relative; font-family: "Open Sans", sans-serif; }

  .card {
    position: absolute;
    left: 276px;
    width: 612px;
    height: 336px;
    background: var(--card);
    border-radius: 26px;
    box-shadow: 0 3px 10px var(--shadow);
    overflow: hidden;
  }
  .card--front { top: 233px; }
  .card--back { top: 643px; height: 341px; }

  .front-band {
    position: absolute;
    left: 0; right: 0; bottom: 0;
    height: 14px;
    background: var(--accent);
  }
  .brand-name {
    position: absolute;
    left: 0; right: 0; top: 146px;
    text-align: center;
    font-family: "Josefin Sans", sans-serif;
    font-weight: 400;
    font-size: 38px;
    letter-spacing: 3px;
    color: var(--brand);
  }

  .back-divider {
    position: absolute;
    left: 288px; top: 10px;
    width: 4px; height: 318px;
    background: var(--accent);
  }
  .tagline {
    position: absolute;
    left: 0; width: 288px; top: 150px;
    text-align: center;
    font-family: "Great Vibes", cursive;
    font-size: 36px;
    color: var(--text-light);
  }
  .brand-small {
    position: absolute;
    left: 0; width: 288px; top: 292px;
    text-align: center;
    font-family: "Josefin Sans", sans-serif;
    font-size: 13px;
    letter-spacing: 1.5px;
    color: var(--brand);
  }

  .contact { position: absolute; left: 324px; top: 42px; color: var(--text); }
  .contact__name { font-size: 26px; line-height: 30px; }
  .contact__role { font-size: 17px; color: var(--text-light); line-height: 24px; }
  .contact__address { margin-top: 56px; font-size: 14px; line-height: 22px; }
  .contact__list { list-style: none; margin-top: 14px; }
  .contact__list li {
    display: flex; align-items: center;
    height: 32px; font-size: 14px;
  }
  .contact__list svg { width: 16px; height: 16px; margin-right: 10px; flex: none; }
</style>
</head>
<body>
  <section class="card card--front" aria-label="Frente do cartão">
    <div class="brand-name">BRILHO MIRIM</div>
    <div class="front-band"></div>
  </section>

  <section class="card card--back" aria-label="Verso do cartão">
    <p class="tagline">Joias Infantis</p>
    <p class="brand-small">BRILHO MIRIM</p>
    <div class="back-divider"></div>

    <div class="contact">
      <p class="contact__name">Nome Completo</p>
      <p class="contact__role">Cargo</p>
      <p class="contact__address">Rua exemplo,Rio de Janeiro -Rj<br>CEP: 0000000.000</p>
      <ul class="contact__list">
        <li>
          <svg viewBox="0 0 16 16"><rect x="4" y="1" width="8" height="14" rx="1.5" fill="none" stroke="var(--accent)" stroke-width="1.6"/><circle cx="8" cy="12.3" r="0.9" fill="var(--accent)"/></svg>
          (00) 9999-0000 / 0000-9999
        </li>
        <li>
          <svg viewBox="0 0 16 16"><rect x="1" y="3" width="14" height="10" rx="1" fill="none" stroke="var(--accent)" stroke-width="1.6"/><path d="M1.5 3.5 8 9l6.5-5.5" fill="none" stroke="var(--accent)" stroke-width="1.6"/></svg>
          Contato@exemplo.com
        </li>
        <li>
          <svg viewBox="0 0 16 16"><rect x="2" y="2" width="12" height="12" rx="2" fill="var(--accent)"/></svg>
          /Exemplo
        </li>
        <li>
          <svg viewBox="0 0 16 16"><circle cx="8" cy="8" r="6.5" fill="none" stroke="var(--accent)" stroke-width="1.5"/><ellipse cx="8" cy="8" rx="2.8" ry="6.5" fill="none" stroke="var(--accent)" stroke-width="1.2"/><path d="M1.5 8h13" stroke="var(--accent)" stroke-width="1.2"/></svg>
          www.brilhomirim.com.br
        </li>
      </ul>
    </div>
  </section>
</body>
</html>
```